Marbleton Solutions Business Card

We need a business card design for a software and IT consulting company called marbleton solutions. We would like to feature a kinkajou (it is a small tree-dwelling animal) somewhere in the design. We would like a green color involved somewhere (but not overwhelming). Back of card should be predominately a color, front of the card can be predominately white or predominately a different color than the back.

Information on front of card:

Contact information:
Phone: (555) 214-3907
Email: peter.dowling@mbtsv.example
Website: www.mbtsv.example

Name: Peter Dowling
Title: Owner / Developer

Information on back of card:
Marbleton Solutions
Targeted Solutions. Fit to your environment.

Industry/Entity Type

Software

Requirements
Should not have
• Avoid anything that too closely resembles a cartoon or campy feel. This should be professional and modern looking.

```html
<!DOCTYPE html>
<html lang="en">
<head>
<meta charset="utf-8">
<title>Marbleton Solutions Business Card</title>
<link rel="stylesheet" href="https://fonts.googleapis.com/css2?family=Lato:wght@300;400&family=Source+Sans+3:wght@400;600&display=swap">
<style>
  :root {
    --backdrop: #e9e7e3;
    --card-white: #ffffff;
    --card-black: #121212;
    --ink-dark: #454545;
    --ink-mid: #7f7f7f;
    --ink-light: #c4c4c4;
    --paper-white: #ffffff;
    --accent-green: #2bb673;
    --edge: #2a2a2a;
  }
  * { margin: 0; padding: 0; box-sizing: border-box; }
  html, body {
    width: 1200px;
    height: 1184px;
    overflow: hidden;
    background: var(--backdrop);
  }
  .stage {
    position: relative;
    width: 1200px;
    height: 1184px;
  }
  .card {
    position: absolute;
    width: 911px;
    height: 520px;
  }
  .card--front {
    left: 46px;
    top: 37px;
    background: var(--card-white);
    border: 1px solid var(--edge);
  }
  .card--back {
    left: 239px;
    top: 604px;
    background: var(--card-black);
  }
  .wordmark {
    font-family: "Lato", sans-serif;
    font-weight: 300;
    letter-spacing: 2px;
    text-transform: uppercase;
    white-space: nowrap;
  }
  .card--front .wordmark {
    position: absolute;
    left: 57px;
    top: 78px;
    font-size: 46px;
    color: var(--ink-mid);
  }
  .holder {
    position: absolute;
    left: 56px;
    top: 272px;
    font-family: "Source Sans 3", sans-serif;
  }
  .holder__name {
    font-size: 32px;
    font-weight: 600;
    color: var(--ink-dark);
    line-height: 1.2;
  }
  .holder__title {
    font-size: 26px;
    color: var(--ink-mid);
    line-height: 1.3;
  }
  .contact-list {
    position: absolute;
    right: 45px;
    top: 270px;
    list-style: none;
    font-family: "Source Sans 3", sans-serif;
    font-size: 26px;
    color: var(--ink-dark);
  }
  .contact-list li {
    display: flex;
    justify-content: flex-end;
    align-items: center;
    gap: 10px;
    height: 44px;
  }
  .contact-list .location {
    margin-top: 48px;
    font-size: 29px;
  }
  .icon {
    width: 22px;
    height: 22px;
    fill: var(--accent-green);
    flex: none;
  }
  .card--back .wordmark {
    position: absolute;
    left: 0;
    right: 0;
    top: 140px;
    text-align: center;
    font-size: 60px;
    font-weight: 400;
    color: var(--paper-white);
  }
  .tagline {
    position: absolute;
    left: 0;
    right: 0;
    top: 270px;
    text-align: center;
    font-family: "Source Sans 3", sans-serif;
    font-size: 40px;
    line-height: 55px;
    text-transform: uppercase;
    color: var(--ink-light);
  }
  .back-url {
    position: absolute;
    left: 0;
    right: 0;
    top: 452px;
    text-align: center;
    font-family: "Source Sans 3", sans-serif;
    font-size: 33px;
    letter-spacing: 3px;
    color: var(--paper-white);
  }
</style>
</head>
<body>
<main class="stage">
  <section class="card card--front">
    <h1 class="wordmark">Marbleton Solutions</h1>
    <div class="holder">
      <p class="holder__name">Peter Dowling</p>
      <p class="holder__title">Owner / Developer</p>
    </div>
    <ul class="contact-list">
      <li>
        <svg class="icon" viewBox="0 0 24 24" aria-hidden="true"><path d="M6.6 10.8a15 15 0 0 0 6.6 6.6l2.2-2.2c.3-.3.7-.4 1-.2 1.1.4 2.3.6 3.6.6.6 0 1 .4 1 1V20c0 .6-.4 1-1 1A17 17 0 0 1 3 4c0-.6.4-1 1-1h3.5c.6 0 1 .4 1 1 0 1.3.2 2.5.6 3.6.1.3 0 .7-.2 1z"/></svg>
        <span>(555) 214-3907</span>
      </li>
      <li>
        <svg class="icon" viewBox="0 0 24 24" aria-hidden="true"><path d="M2 7l10 6 10-6v12H2z"/><path d="M2 5h20L12 11z"/></svg>
        <span>peter.dowling@mbtsv.example</span>
      </li>
      <li>
        <svg class="icon" viewBox="0 0 24 24" aria-hidden="true" fill="none"><g fill="none" stroke="#2bb673" stroke-width="1.6"><circle cx="12" cy="12" r="9"/><ellipse cx="12" cy="12" rx="4" ry="9"/><path d="M3 12h18M5 7h14M5 17h14"/></g></svg>
        <span>www.mbtsv.example</span>
      </li>
      <li class="location">
        <svg class="icon" viewBox="0 0 24 24" aria-hidden="true"><path d="M12 2a7 7 0 0 0-7 7c0 5 7 13 7 13s7-8 7-13a7 7 0 0 0-7-7zm0 9.5A2.5 2.5 0 1 1 12 6.5a2.5 2.5 0 0 1 0 5z"/></svg>
        <span>Lakemont, TX</span>
      </li>
    </ul>
  </section>

  <section class="card card--back">
    <h2 class="wordmark">Marbleton Solutions</h2>
    <p class="tagline">Targeted Solutions<br>Fit to your environment</p>
    <p class="back-url">www.mbtsv.example</p>
  </section>
</main>
</body>
</html>
```